Business card design needed

I am a free lance management consultant looking to have some professionally designed business cards created.
If possible if i could have some bullet points or something with a list of my services that would be great.
Services are:
- Strategic Planning
- Process Improvement
- Change Management
- IT Solutions & Implementation
- IT Consulting
- Web Solutions
Target Market(s)
Business Owners and Operators
Industry/Entity Type
Business
Contact Information for Business Card
Peter Whitlock
PW Consulting
0438 516 274
PETER@PETERWHITLOCK.EXAMPLE
www.peterwhitlock.example
Logo Text
PW Consulting
Logo styles of interest
Pictorial/Combination Logo
Wordmark Logo
Lettermark Logo
Look and feel
Each slider illustrates characteristics of the customer's brand and the style your logo design should communicate.

```html
<!DOCTYPE html>
<html lang="en">
<head>
<meta charset="utf-8">
<title>Peter Whitlock – Business Card</title>
<link rel="stylesheet" href="https://fonts.googleapis.com/css2?family=Cinzel:wght@400&family=Source+Sans+3:wght@400&display=swap">
<style>
  :root {
    --paper: #ffffff;
    --ink: #111111;
    --lime: #d2f863;
  }
  html, body {
    margin: 0;
    padding: 0;
    overflow: hidden;
    background: var(--paper);
  }
  .card {
    position: relative;
    width: 1200px;
    height: 693px;
    background: var(--paper);
    color: var(--ink);
    overflow: hidden;
    font-family: "Source Sans 3", "Myriad Pro", sans-serif;
  }
  .card__name {
    position: absolute;
    left: 34px;
    top: 24px;
    margin: 0;
    font-family: "Cinzel", "Trajan Pro", serif;
    font-weight: 400;
    font-size: 62px;
    letter-spacing: 2px;
    line-height: 1;
    text-transform: uppercase;
    white-space: nowrap;
  }
  .card__brand {
    position: absolute;
    right: 22px;
    top: 248px;
    margin: 0;
    font-family: "Cinzel", "Trajan Pro", serif;
    font-weight: 400;
    font-size: 38px;
    line-height: 1;
    color: var(--lime);
    white-space: nowrap;
  }
  .card__contact {
    position: absolute;
    left: 51px;
    top: 386px;
    margin: 0;
    font-size: 30px;
    line-height: 48px;
  }
  .card__contact-row {
    white-space: nowrap;
  }
  .card__contact-label,
  .card__contact-value {
    display: inline;
    margin: 0;
  }
  .card__contact-row--email .card__contact-value {
    font-size: 27px;
  }
  .card__services {
    position: absolute;
    left: 697px;
    top: 306px;
    margin: 0;
    padding: 0;
    list-style: none;
    font-size: 33px;
    line-height: 45.5px;
    white-space: nowrap;
  }
  .card__services li::before {
    content: "- ";
  }
  .card__web {
    position: absolute;
    left: 0;
    width: 1200px;
    top: 616px;
    margin: 0;
    text-align: center;
    font-size: 46px;
    line-height: 1;
    white-space: nowrap;
  }
</style>
</head>
<body>
  <main class="card">
    <h1 class="card__name">Peter Whitlock</h1>

    <p class="card__brand">PW Consulting</p>

    <dl class="card__contact">
      <div class="card__contact-row">
        <dt class="card__contact-label">phone : </dt><dd class="card__contact-value">0438 516 274</dd>
      </div>
      <div class="card__contact-row card__contact-row--email">
        <dt class="card__contact-label">email&nbsp;&nbsp;&nbsp;: </dt><dd class="card__contact-value">PETER@PETERWHITLOCK.EXAMPLE</dd>
      </div>
    </dl>

    <ul class="card__services">
      <li>Strategic Planning</li>
      <li>Process Improvement</li>
      <li>Change Management</li>
      <li>IT Solutions &amp; Implementation</li>
      <li>IT Consulting</li>
      <li>Web Solutions</li>
    </ul>

    <p class="card__web">web : www.peterwhitlock.example</p>
  </main>
</body>
</html>
```